Can Design for Fun, Growing Health Food Brand

We are launching a brand new product, electrolyte seltzer drinks. We want the design to be clean/simple and slightly modern while staying true to our brand identity. Must say "Mineral Hydration" as the product descriptor, sub headline is "Carbonated electrolyte beverage with sea moss and real fruit juice". First flavors will be Watermelon Mint and Mango.

Target Market(s)

Women ages 30-50 who are interested in health wellness/trends

Industry/Entity Type

Health & Wellness

Font styles to use
Sans Serif

Requirements
Must have
• Tall, skinny can, current Bright Kelp Co Logo, use aluminum on can as element in design.
Nice to have
• Be fun, clean and modern. Would like to see the label less busy than our gels.
Should not have
• Avoid putting flavor on bottom 1/5 of can. No gradient color changes. Do not want really detailed or realistic fruit image, prefer drawings or similar.

```html
<!DOCTYPE html>
<html lang="en">
<head>
<meta charset="utf-8">
<title>Bright Kelp Co — Mineral Hydration Can Labels</title>
<link rel="stylesheet" href="https://fonts.googleapis.com/css2?family=Oswald:wght@300;400;600;700&family=Open+Sans:wght@400&display=swap">
<style>
  :root {
    --page: #ffffff;
    --aluminum: #d6dadd;
    --aluminum-rim: #8e9498;
    --melon: #5fe278;
    --melon-ink: #2f8a5d;
    --melon-art: #9ff0ad;
    --mango: #ef6b40;
    --mango-ink: #e0603a;
    --mango-art: #f7a383;
    --white: #ffffff;
    --caption: #111111;
  }
  * { box-sizing: border-box; margin: 0; padding: 0; }
  html, body { width: 1200px; height: 846px; overflow: hidden; background: var(--page); }
  body { position: relative; font-family: "Oswald", "Arial Narrow", sans-serif; color: var(--white); }

  .label {
    position: absolute; top: 72px; width: 262px; height: 663px;
    border-radius: 18px 18px 22px 22px; overflow: hidden;
    background: var(--aluminum);
  }
  .label--melon-front { left: 31px; }
  .label--melon-back  { left: 320px; }
  .label--mango-front { left: 619px; }
  .label--mango-back  { left: 908px; }

  .rim { position: absolute; left: 30px; right: 30px; top: 0; height: 10px; background: var(--aluminum-rim); border-radius: 4px; }
  .body-field { position: absolute; left: 0; top: 0; width: 262px; height: 663px; }
  .theme-melon .body-field path { fill: var(--melon); }
  .theme-mango .body-field path { fill: var(--mango); }

  .art { position: absolute; border-radius: 50%; }
  .theme-melon .art { background: var(--melon-art); }
  .theme-mango .art { background: var(--mango-art); }

  .vertical {
    position: absolute; writing-mode: vertical-rl; transform: rotate(180deg);
    white-space: nowrap; line-height: 1;
  }
  .front-brand { left: 52px; bottom: 96px; font-weight: 300; font-size: 62px; letter-spacing: -1px; }
  .front-descriptor { left: 118px; bottom: 106px; font-weight: 400; font-size: 42px; letter-spacing: 0.5px; }
  .front-flavor {
    left: 177px; top: 400px; width: 34px; height: 152px; border-radius: 9px;
    background: var(--white); font-family: "Oswald", sans-serif; font-weight: 700; font-size: 15px;
    display: flex; align-items: center; justify-content: center;
  }
  .theme-melon .front-flavor, .theme-melon .back-flavor { color: var(--melon-ink); }
  .theme-mango .front-flavor, .theme-mango .back-flavor { color: var(--mango-ink); }
  .volume { position: absolute; left: 0; right: 0; top: 594px; text-align: center; font-weight: 300; font-size: 20px; word-spacing: 6px; }

  .back-stack { position: absolute; left: 0; right: 0; top: 103px; text-align: center; }
  .brand-mark { width: 34px; height: 34px; border-radius: 50%; border: 2px solid var(--white); margin: 0 auto 8px; }
  .brand-name { font-weight: 300; font-size: 30px; letter-spacing: -1px; line-height: 1; }
  .back-descriptor { margin-top: 16px; font-weight: 600; font-size: 38px; line-height: 36px; }
  .back-flavor {
    display: inline-block; margin-top: 20px; width: 152px; height: 32px; line-height: 32px;
    border-radius: 9px; background: var(--white); font-weight: 700; font-size: 16px;
  }
  .back-sub { margin-top: 14px; font-weight: 300; font-size: 21px; line-height: 24px; }

  .caption {
    position: absolute; top: 790px; width: 262px; text-align: center;
    font-family: "Open Sans", Arial, sans-serif; font-size: 17px; color: var(--caption);
  }
</style>
</head>
<body>

  <!-- Watermelon Mint front -->
  <section class="label label--melon-front theme-melon">
    <svg class="body-field" viewBox="0 0 262 663"><path d="M0 81 H262 V648 H0 Z"/></svg>
    <div class="rim"></div>
    <div class="art" role="img" aria-label="Line drawing of a watermelon slice with mint leaves" style="left:55px;top:50px;width:152px;height:118px;"></div>
    <div class="vertical front-brand">BRIGHT KELP CO</div>
    <div class="vertical front-descriptor">MINERAL HYDRATION</div>
    <div class="vertical front-flavor">WATERMELON MINT</div>
    <p class="volume">12oz | 355ml</p>
  </section>

  <!-- Watermelon Mint back -->
  <section class="label label--melon-back theme-melon">
    <svg class="body-field" viewBox="0 0 262 663"><path d="M0 81 C60 81 80 71 131 71 C182 71 202 81 262 81 V648 H0 Z"/></svg>
    <div class="rim"></div>
    <div class="back-stack">
      <div class="brand-mark"></div>
      <p class="brand-name">BRIGHT KELP CO</p>
      <h2 class="back-descriptor">MINERAL<br>HYDRATION</h2>
      <span class="back-flavor">WATERMELON MINT</span>
      <p class="back-sub">CARBONATED<br>ELECTROLYTE<br>BEVERAGE WITH<br>SEA MOSS AND<br>REAL FRUIT JUICE</p>
    </div>
    <div class="art" role="img" aria-label="Line drawing of a watermelon slice with mint leaves" style="left:43px;top:469px;width:176px;height:130px;"></div>
  </section>

  <!-- Mango front -->
  <section class="label label--mango-front theme-mango">
    <svg class="body-field" viewBox="0 0 262 663"><path d="M0 81 H262 V648 H0 Z"/></svg>
    <div class="rim"></div>
    <div class="art" role="img" aria-label="Line drawing of a whole mango and a halved mango with leaves" style="left:62px;top:38px;width:136px;height:134px;"></div>
    <div class="vertical front-brand">BRIGHT KELP CO</div>
    <div class="vertical front-descriptor">MINERAL HYDRATION</div>
    <div class="vertical front-flavor">MANGO</div>
    <p class="volume">12oz | 355ml</p>
  </section>

  <!-- Mango back -->
  <section class="label label--mango-back theme-mango">
    <svg class="body-field" viewBox="0 0 262 663"><path d="M0 81 C60 81 80 71 131 71 C182 71 202 81 262 81 V648 H0 Z"/></svg>
    <div class="rim"></div>
    <div class="back-stack">
      <div class="brand-mark"></div>
      <p class="brand-name">BRIGHT KELP CO</p>
      <h2 class="back-descriptor">MINERAL<br>HYDRATION</h2>
      <span class="back-flavor">MANGO</span>
      <p class="back-sub">CARBONATED<br>ELECTROLYTE<br>BEVERAGE WITH<br>SEA MOSS AND<br>REAL FRUIT JUICE</p>
    </div>
    <div class="art" role="img" aria-label="Line drawing of a whole mango and a halved mango with leaves" style="left:62px;top:466px;width:138px;height:136px;"></div>
  </section>

  <p class="caption" style="left:31px;">WATERMELON MINT FRONT</p>
  <p class="caption" style="left:320px;">WATERMELON MINT BACK</p>
  <p class="caption" style="left:619px;">MANGO FRONT</p>
  <p class="caption" style="left:908px;">MANGO BACK</p>

</body>
</html>
```